Corvane Communications ISP Flyer

Our company is Corvane Communications. We need to create a flyer to market our Internet/Phone services to a retirement community. We will be offering 50x50 internet connection along with a single phone line for $49.99 (before taxes). We would like to emphasize that our services are over fiber optic cables.

Internet Service
- 50x50 megabit fiber internet connection
- up to 5 email addresses
- 10gb of online storage

Phone Service
- Local 956 Phone number
- Unlimited Local/Long distance
- Caller Id
- Web access to Voicemail

Target Market(s)

Residential Customers

Industry/Entity Type

Internet

Requirements
Must have
• Company Name - Corvane Communications
Service detail

Contact info -

sales@corvaneco.example
956-483-2619

```html
<!DOCTYPE html>
<html lang="en">
<head>
<meta charset="utf-8">
<title>Corvane Communications – Internet &amp; Phone Flyer</title>
<link rel="stylesheet" href="https://fonts.googleapis.com/css2?family=Oswald:wght@500;700&family=Roboto+Condensed:wght@400&family=Open+Sans:wght@700&display=swap">
<style>
  :root {
    --page-bg: #ececec;
    --paper: #ffffff;
    --ink: #2b2b2b;
    --ink-soft: #4a4a4a;
    --photo-light: #e4e7ea;
    --photo-mid: #cdb9a1;
    --photo-warm: #a88868;
    --photo-cool: #b9c3cc;
  }
  * { margin: 0; padding: 0; box-sizing: border-box; }
  html, body {
    width: 1200px;
    height: 800px;
    overflow: hidden;
    background: var(--page-bg);
  }
  .flyer {
    position: absolute;
    left: 60px;
    top: 40px;
    width: 1080px;
    height: 720px;
    background: var(--paper);
    box-shadow: 0 6px 18px rgba(0,0,0,0.18);
    overflow: hidden;
  }
  .flyer__photo {
    position: absolute;
    inset: 0;
    width: 1080px;
    height: 720px;
  }
  .flyer__content {
    position: absolute;
    left: 60px;
    top: 56px;
    width: 460px;
    color: var(--ink);
  }
  .brand {
    font-family: "Oswald", sans-serif;
    font-weight: 700;
    text-transform: uppercase;
    line-height: 0.95;
    letter-spacing: 1px;
  }
  .brand__first { display: block; font-size: 40px; color: var(--ink-soft); }
  .brand__second { display: block; font-size: 64px; }
  .service { margin-top: 48px; }
  .service + .service { margin-top: 30px; }
  .service__title {
    font-family: "Oswald", sans-serif;
    font-weight: 500;
    font-size: 30px;
    letter-spacing: 1.5px;
    text-transform: uppercase;
    margin-bottom: 6px;
  }
  .service__list {
    list-style: none;
    font-family: "Roboto Condensed", sans-serif;
    font-size: 21px;
    line-height: 1.35;
    color: var(--ink-soft);
  }
  .service__list li::before { content: "- "; }
  .contact {
    position: absolute;
    left: 60px;
    bottom: 52px;
    font-family: "Open Sans", sans-serif;
    font-weight: 700;
    font-size: 22px;
    line-height: 1.35;
    color: var(--ink);
  }
</style>
</head>
<body>
  <article class="flyer">
    <svg class="flyer__photo" viewBox="0 0 1080 720" role="img" aria-label="Photo of a smiling older man relaxing on a striped sofa at home, holding a tablet and a phone">
      <defs>
        <linearGradient id="photoTone" x1="0" y1="0" x2="1" y2="1">
          <stop offset="0" stop-color="var(--photo-cool)"/>
          <stop offset="0.35" stop-color="var(--photo-light)"/>
          <stop offset="0.7" stop-color="var(--photo-mid)"/>
          <stop offset="1" stop-color="var(--photo-warm)"/>
        </linearGradient>
      </defs>
      <path d="M560 0 H1080 V720 H520 C660 560 700 380 640 200 C615 120 585 60 560 0 Z" fill="url(#photoTone)"/>
    </svg>

    <div class="flyer__content">
      <h1 class="brand">
        <span class="brand__first">Corvane</span>
        <span class="brand__second">Communications</span>
      </h1>

      <section class="service">
        <h2 class="service__title">Internet Service</h2>
        <ul class="service__list">
          <li>50x50 megabit fiber internet connection</li>
          <li>up to 5 email addresses</li>
          <li>10gb of online storage</li>
        </ul>
      </section>

      <section class="service">
        <h2 class="service__title">Phone Service</h2>
        <ul class="service__list">
          <li>Local 956 Phone number</li>
          <li>Unlimited Local/Long distance</li>
          <li>Caller Id</li>
          <li>Web access to Voicemail</li>
        </ul>
      </section>
    </div>

    <address class="contact">
      sales@corvaneco.example<br>
      956-483-2619
    </address>
  </article>
</body>
</html>
```